English and Spanish Language School Needs a Business Card

Need a business card design a startup company called Meridel Language School. The company will offer English and Spanish conversational level courses designed to make the learner feel comfortable with grammar and vocabulary. We would like to see a logo with some colour that should communicate learning, growth.

Target Market(s)

Consumers and businesses

Industry/Entity Type

Education

Contact Information for Business Card

TBD

Font styles to use
Serif

Requirements
Must have
• Include the following
• Logo
• Name
• Title
• Cellphone Number
• Office Phone number
• Email address
• Office Address

```html
<!DOCTYPE html>
<html lang="en">
<head>
<meta charset="utf-8">
<title>Meridel Language School – Business Card</title>
<link href="https://fonts.googleapis.com/css2?family=Lato:wght@400;700;900&display=swap" rel="stylesheet">
<style>
  :root {
    --backdrop: #2a2c2f;
    --brand-red: #c51f27;
    --accent-soft-red: #d9705a;
    --accent-soft-white: #fbece7;
    --card-white: #ffffff;
    --ink: #1d1d1f;
    --teal: #1a9ba6;
    --shadow: rgba(0, 0, 0, 0.45);
  }
  * { margin: 0; padding: 0; box-sizing: border-box; }
  html, body {
    width: 1200px;
    height: 900px;
    overflow: hidden;
    background: var(--backdrop);
    font-family: "Lato", sans-serif;
  }
  .canvas {
    position: relative;
    width: 1200px;
    height: 900px;
  }
  .card {
    position: absolute;
    left: 330px;
    width: 540px;
    height: 310px;
    border-radius: 26px;
    box-shadow: 0 14px 30px var(--shadow);
    overflow: hidden;
  }
  .accent-circle {
    position: absolute;
    width: 300px;
    height: 300px;
    border-radius: 50%;
    right: -110px;
    bottom: -150px;
  }
  /* Back side */
  .card-back {
    top: 90px;
    background: var(--brand-red);
  }
  .card-back .accent-circle { background: var(--accent-soft-red); opacity: 0.75; }
  .card-back .wordmark {
    position: absolute;
    left: 60px;
    top: 78px;
    color: var(--card-white);
    font-weight: 900;
    font-size: 44px;
    line-height: 1.08;
    letter-spacing: 0.5px;
  }
  /* Front side */
  .card-front {
    top: 490px;
    background: var(--card-white);
  }
  .card-front .accent-circle { background: var(--accent-soft-white); }
  .card-front .wordmark {
    position: absolute;
    left: 34px;
    top: 104px;
    width: 200px;
    color: var(--brand-red);
    font-weight: 900;
    font-size: 28px;
    line-height: 1.1;
  }
  .divider {
    position: absolute;
    left: 252px;
    top: 0;
    width: 2px;
    height: 268px;
    background: var(--brand-red);
  }
  .divider-notch {
    position: absolute;
    left: 244px;
    top: 0;
    width: 0;
    height: 0;
    border-left: 9px solid transparent;
    border-right: 9px solid transparent;
    border-top: 14px solid var(--brand-red);
  }
  .contact {
    position: absolute;
    left: 272px;
    top: 40px;
    color: var(--ink);
  }
  .contact .person-name {
    font-weight: 700;
    font-size: 27px;
    letter-spacing: 0.5px;
  }
  .contact .person-title {
    font-size: 19px;
    margin-top: 2px;
    margin-bottom: 16px;
  }
  .contact-list { list-style: none; }
  .contact-list li {
    display: flex;
    align-items: center;
    gap: 9px;
    font-size: 15.5px;
    margin-bottom: 8px;
  }
  .contact-list li.address { align-items: flex-start; }
  .icon {
    flex: 0 0 22px;
    width: 22px;
    height: 22px;
  }
</style>
</head>
<body>
<main class="canvas">

  <section class="card card-back" aria-label="Business card back">
    <div class="accent-circle"></div>
    <p class="wordmark">Meridel<br>Language School</p>
  </section>

  <section class="card card-front" aria-label="Business card front">
    <div class="accent-circle"></div>
    <p class="wordmark">Meridel Language School</p>
    <div class="divider-notch"></div>
    <div class="divider"></div>

    <div class="contact">
      <h1 class="person-name">Tobias Marlow</h1>
      <p class="person-title">Trainer</p>
      <ul class="contact-list">
        <li>
          <svg class="icon" viewBox="0 0 22 22" aria-hidden="true">
            <circle cx="11" cy="11" r="11" fill="var(--teal)"/>
            <rect x="7.5" y="5" width="7" height="12" rx="1.3" fill="none" stroke="#fff" stroke-width="1.4"/>
            <circle cx="11" cy="15" r="0.8" fill="#fff"/>
          </svg>
          +00 415 278 9036
        </li>
        <li>
          <svg class="icon" viewBox="0 0 22 22" aria-hidden="true">
            <circle cx="11" cy="11" r="11" fill="var(--teal)"/>
            <path d="M7.5 6.2c.6-.6 1.4-.5 1.8.1l1 1.6c.3.5.2 1.1-.2 1.5l-.6.5c.6 1.2 1.5 2.1 2.7 2.7l.5-.6c.4-.4 1-.5 1.5-.2l1.6 1c.6.4.7 1.2.1 1.8l-.8.8c-.8.8-2.3.6-4.1-.6-1.1-.8-2.1-1.8-2.9-2.9-1.2-1.8-1.4-3.3-.6-4.1z" fill="#fff"/>
          </svg>
          +00 52937184
        </li>
        <li>
          <svg class="icon" viewBox="0 0 22 22" aria-hidden="true">
            <circle cx="11" cy="11" r="11" fill="var(--teal)"/>
            <rect x="5.5" y="7" width="11" height="8" fill="none" stroke="#fff" stroke-width="1.3"/>
            <path d="M5.5 7l5.5 4.5L16.5 7" fill="none" stroke="#fff" stroke-width="1.3"/>
          </svg>
          tmarlow@meridel-school.test
        </li>
        <li class="address">
          <svg class="icon" viewBox="0 0 22 22" aria-hidden="true">
            <circle cx="11" cy="11" r="11" fill="var(--teal)"/>
            <path d="M11 5a3.3 3.3 0 0 0-3.3 3.3c0 2.5 3.3 6 3.3 6s3.3-3.5 3.3-6A3.3 3.3 0 0 0 11 5z" fill="#fff"/>
            <circle cx="11" cy="8.3" r="1.2" fill="var(--teal)"/>
            <ellipse cx="11" cy="16" rx="4" ry="1.2" fill="none" stroke="#fff" stroke-width="1"/>
          </svg>
          <span>48 Alder Lane, Westbrook,<br>Northland</span>
        </li>
      </ul>
    </div>
  </section>

</main>
</body>
</html>
```